Vantora88 - a Political Plebescite app.

There is a current app in the App Store (worldwide) and Play Store (worldwide) called yourBallot (with an owl logo). The UX needs to be redesigned to make it more visually pleasing.

The requirement is to build a UX that is suitable for both iOS and Android - i.e. consistent look for both platforms. The design is to span the variety of sizes available from smart devices - phones and tablets. The layout as it stands is portrait only, and a secondary design to encompass landscape is wanted.

You would need to download the app to get a feel for all the functionality - there are 3 visible forms (currently) and a hidden form, that will be used in the near future - this hidden form will look similar to the main (first) form.

To get full functionality you need to do the following:
Go to the Options page
Toggle the top slide
Click on UNREGISTERED
Select a state/territory

I know this is a bit non-intuitive - in the "real" product these steps are automated - but for this release the user gets to choose.

Once this is done - the other button(s) appear in the top left of the screen - and data is available to be displayed.

The current forms are included in this brief. The Options screen will ultimately not be showing all the current data, only the lower slider (or other indicator) and the associated version and copyright notices. The hidden screen is much like the main screen - showing the name of the bill and information pertaining to that bill - there needs to be a button (or action site) to toggle between the main and this hidden screen.

Target Market(s)

All eligable voters (currently in Australia)

Industry/Entity Type

Political

Requirements
Should not have
• Do not present to me my own/existing design with the only change being colours and label layout.

```html
<!DOCTYPE html>
<html lang="en">
<head>
<meta charset="utf-8">
<title>yourBallot – app screens</title>
<link href="https://fonts.googleapis.com/css2?family=Lato:wght@400;700&display=swap" rel="stylesheet">
<style>
:root{
  --backdrop:#1b1f27;
  --backdrop-2:#2a303a;
  --screen:#f4f4f4;
  --white:#ffffff;
  --ink:#333333;
  --muted:#9a9a9a;
  --rule:#dddddd;
  --teal:#0aa39a;
  --red:#e8505b;
  --blue:#2f4c9c;
  --brand:#1f8fe0;
  --pill:#aaaaaa;
  --overlay:#6a6a6a;
}
*{box-sizing:border-box;margin:0;padding:0}
html,body{width:1200px;height:1200px;overflow:hidden}
body{font-family:'Lato',sans-serif;color:var(--ink);position:relative}
.backdrop{position:absolute;inset:0;background:linear-gradient(180deg,var(--backdrop) 0%,var(--backdrop-2) 55%,var(--backdrop) 100%)}
.screen{position:absolute;width:321px;height:571px;background:var(--screen);overflow:hidden}
.splash{left:39px;top:26px;background:var(--white)}
.main{left:430px;top:26px}
.menu{left:822px;top:26px}
.setting{left:244px;top:610px}
.info{left:636px;top:610px}

.status{position:absolute;top:0;left:0;right:0;height:16px;background:var(--white);font-size:9px;display:flex;justify-content:space-between;align-items:center;padding:0 6px}
.status .battery{display:inline-block;width:16px;height:7px;border:1px solid #333;vertical-align:middle;margin-left:3px;position:relative}
.status .battery::after{content:"";position:absolute;left:1px;top:1px;bottom:1px;width:9px;background:#333}
.header{position:absolute;top:16px;left:0;right:0;height:42px;background:var(--white);display:flex;align-items:center;justify-content:center}
.header .title{font-size:14px;letter-spacing:.5px}
.header .regions{position:absolute;left:10px;top:12px;display:flex;gap:4px}
.region{width:19px;height:15px;border-radius:5px}
.region.fed{background:#b0b0b0}
.region.state{background:var(--red)}
.header .control{position:absolute;right:14px;top:13px}

.brand{position:absolute;left:0;right:0;top:268px;text-align:center}
.brand .mark{width:52px;height:52px;border-radius:50%;background:var(--brand);margin:0 auto 8px}
.brand .name{font-size:24px;color:var(--brand);font-weight:400}

.bill-title{position:absolute;left:16px;top:80px;font-size:12px;font-weight:700;color:#3a3a3a}
.bill-doc{position:absolute;right:16px;top:80px}
.bill-rule{position:absolute;left:19px;right:19px;top:118px;border-top:1px solid var(--rule)}
.bill-desc{position:absolute;left:18px;right:18px;top:136px;font-size:8.5px;line-height:15px;color:var(--muted);text-align:center}
.votes{position:absolute;top:504px;left:16px;right:19px;display:flex;justify-content:space-between}
.vote{width:85px;height:28px;border-radius:14px;color:var(--white);font-size:13px;display:flex;align-items:center;justify-content:center}
.vote.no,.vote.party{background:var(--pill)}
.vote.yes{background:var(--teal)}
.footer{position:absolute;top:545px;left:0;right:0;height:16px;display:flex;align-items:center;font-size:9.5px;color:var(--muted);padding:0 21px 0 17px}
.footer .dot{width:8px;height:8px;border-radius:50%;background:var(--teal);margin-right:17px}
.footer .count{margin-left:auto}

.shade{position:absolute;left:0;right:0;top:58px;bottom:0;background:var(--overlay)}
.shade .votes .vote{background:#555;color:#6f6f6f}
.shade .votes .vote.yes{background:#0f4e4b}
.shade .footer{color:#555;top:487px}
.shade .footer .dot{background:#0f4e4b}
.shade .votes{top:446px}
.menu-panel{position:absolute;left:0;right:0;top:58px;height:127px;background:var(--blue);display:flex}
.menu-item{flex:1;display:flex;flex-direction:column;align-items:center;padding-top:34px;color:var(--white);font-size:11.5px;font-weight:700}
.menu-item svg{margin-bottom:8px}
.menu-panel .divider{width:1px;background:#4f69b3;margin:10px 0}

.section{position:absolute;left:0;right:0;height:22px;background:var(--white);font-size:8px;font-weight:700;padding:6px 21px;color:#333}
.row{position:absolute;left:29px;right:18px;font-size:11.5px;color:var(--muted);display:flex;align-items:center;justify-content:space-between}
.toggle{width:36px;height:12px;border-radius:6px;position:relative}
.toggle::after{content:"";position:absolute;top:-3px;width:18px;height:18px;border-radius:50%}
.toggle.on{background:#5fd6cf}
.toggle.on::after{right:0;background:var(--teal)}
.toggle.off{background:#cfcfcf}
.toggle.off::after{left:0;background:#e8e8e8}
.detail{position:absolute;left:29px;font-size:11.5px;color:var(--muted)}
.detail b{position:absolute;left:150px;font-weight:400;color:#333;white-space:nowrap}
.credits{position:absolute;left:0;right:0;top:451px;font-size:9.5px;line-height:15px;text-align:center;color:#333}
.credits a{color:var(--red);text-decoration:none}

.tabs{position:absolute;top:76px;left:3px;right:3px;display:flex;font-size:12px;color:var(--muted)}
.tab{flex:1;text-align:center;padding-bottom:6px}
.tab.active{color:#333;border-bottom:3px solid var(--red)}
.about{position:absolute;left:10px;right:14px;top:116px;font-size:8.5px;line-height:15.2px;text-transform:uppercase;text-align:justify;color:#555}
.about p+p{margin-top:15px}
</style>
</head>
<body>
<div class="backdrop" role="img" aria-label="Dark evening photograph of a harbour city skyline behind the screens"></div>

<section class="screen splash">
  <div class="brand">
    <div class="mark"></div>
    <div class="name">yourBallot</div>
  </div>
</section>

<section class="screen main">
  <div class="status"><span>●●●●● Carrier</span><span>9:23 AM</span><span>66%<i class="battery"></i></span></div>
  <header class="header">
    <div class="regions"><div class="region fed" role="img" aria-label="Federal region map icon"></div><div class="region state" role="img" aria-label="State region map icon"></div></div>
    <span class="title">MAIN</span>
    <svg class="control" width="18" height="15"><rect y="0" width="18" height="2.5" fill="#333"/><rect y="6" width="18" height="2.5" fill="#333"/><rect y="12" width="18" height="2.5" fill="#333"/></svg>
  </header>
  <h1 class="bill-title">Crimes Amendment (Ava's Law) Bill 2015</h1>
  <svg class="bill-doc" width="13" height="17"><rect width="13" height="17" fill="#fff"/><g fill="var(--teal)"><rect x="2" y="6" width="9" height="1.2"/><rect x="2" y="8.5" width="9" height="1.2"/><rect x="2" y="11" width="9" height="1.2"/><rect x="2" y="13.5" width="9" height="1.2"/></g></svg>
  <div class="bill-rule"></div>
  <p class="bill-desc">An Act to amend the Crimes Act 1900 to prohibit conduct that causes serious harm to or the destruction of a child in utero; and for other purpose s</p>
  <div class="votes"><div class="vote no">NO</div><div class="vote party">PARTY</div><div class="vote yes">YES</div></div>
  <div class="footer"><span class="dot"></span>Legislative Council<span class="count">1/77</span></div>
</section>

<section class="screen menu">
  <div class="status"><span>●●●●● Carrier</span><span>9:23 AM</span><span>66%<i class="battery"></i></span></div>
  <header class="header">
    <div class="regions"><div class="region fed" role="img" aria-label="Federal region map icon"></div><div class="region state" role="img" aria-label="State region map icon"></div></div>
    <span class="title">MAIN</span>
    <svg class="control" width="18" height="18"><path d="M1 1L17 17M17 1L1 17" stroke="#333" stroke-width="2.6"/></svg>
  </header>
  <div class="shade">
    <div class="votes"><div class="vote no">NO</div><div class="vote party">PARTY</div><div class="vote yes">YES</div></div>
    <div class="footer"><span class="dot"></span>Legislative Council<span class="count">1/77</span></div>
  </div>
  <nav class="menu-panel">
    <div class="menu-item">
      <svg width="38" height="38" viewBox="0 0 38 38"><circle cx="19" cy="19" r="6" fill="none" stroke="#fff" stroke-width="2"/><circle cx="19" cy="19" r="12" fill="none" stroke="#fff" stroke-width="2" stroke-dasharray="5 4.4"/><circle cx="19" cy="19" r="15" fill="none" stroke="#fff" stroke-width="2" stroke-dasharray="4.2 5.2"/></svg>
      SETTING OPTION
    </div>
    <div class="divider"></div>
    <div class="menu-item">
      <svg width="38" height="38" viewBox="0 0 38 38"><circle cx="19" cy="19" r="17" fill="none" stroke="#fff" stroke-width="2.4"/><circle cx="20" cy="11" r="2.2" fill="#fff"/><path d="M17 16h4v11h2" stroke="#fff" stroke-width="3" fill="none"/></svg>
      INFO
    </div>
  </nav>
</section>

<section class="screen setting">
  <div class="status"><span>●●●●● Carrier</span><span>9:23 AM</span><span>66%<i class="battery"></i></span></div>
  <header class="header">
    <div class="regions"><div class="region fed" role="img" aria-label="Federal region map icon"></div><div class="region state" role="img" aria-label="State region map icon"></div></div>
    <span class="title">SETTING</span>
    <svg class="control" width="18" height="15"><rect y="0" width="18" height="2.5" fill="#333"/><rect y="6" width="18" height="2.5" fill="#333"/><rect y="12" width="18" height="2.5" fill="#333"/></svg>
  </header>
  <div class="section" style="top:70px">DISPLAY</div>
  <div class="row" style="top:112px">Display User GUIDs<span class="toggle on"></span></div>
  <div class="row" style="top:146px">Hide Bills after Opinion<span class="toggle off"></span></div>
  <div class="section" style="top:186px">REPRESENTATIVE DETAILS</div>
  <div class="detail" style="top:228px">Federal Region<b>yourBallot_Federal</b></div>
  <div class="detail" style="top:254px">Federal Representative<b>Aust. Masked Owl</b></div>
  <div class="detail" style="top:280px">State Region<b>yourBallot_NSW</b></div>
  <div class="detail" style="top:306px">State Representative<b>Lesser Sooty Owl</b></div>
  <div class="credits">
    v0.752<br>Federal Bil Details © Federal Bill Registry.<br><a>http://www.fedbills.example.au</a><br>State Bill Details © State Bill Registry (State Assembly).<br><a>http://www.statebills.example.au</a>
  </div>
  <div class="footer"><span class="dot"></span>Legislative Council<span class="count">1/77</span></div>
</section>

<section class="screen info">
  <div class="status"><span>●●●●● Carrier</span><span>9:23 AM</span><span>66%<i class="battery"></i></span></div>
  <header class="header">
    <div class="regions"><div class="region fed" role="img" aria-label="Federal region map icon"></div><div class="region state" role="img" aria-label="State region map icon"></div></div>
    <span class="title">INFO</span>
    <svg class="control" width="18" height="15"><rect y="0" width="18" height="2.5" fill="#333"/><rect y="6" width="18" height="2.5" fill="#333"/><rect y="12" width="18" height="2.5" fill="#333"/></svg>
  </header>
  <div class="tabs"><div class="tab active">GENERAL</div><div class="tab">FAQ</div><div class="tab">CONTACT</div></div>
  <div class="about">
    <p>Lorem Ipsum is simply dummy text of the printing and typesetting industry. Lorem Ipsum has been the industry's standard dummy text ever since the 1500s, when an unknown printer took a galley of type and scrambled it to make a type specimen book. It has survived not only five centuries, but also the leap into electronic typesetting, remaining essentially unchanged. It was popularised in the 1960s with the release of Transfa sheets containing Lorem Ipsum passages, and more recently with desktop publishing software like Quillset Layout including versions of Lorem Ipsum.</p>
    <p>Contrary to popular belief, Lorem Ipsum is not simply random text. It has roots in a piece of classical Latin literature from 45 BC, making it over 2000 years old. Harold Vinter, a Latin professor at Halden Vale College in Virginia, looked up one of the more obscure Latin words, consectetur, from a Lorem Ipsum passage, and going through the cites of the word in classical literature, discovered the undoubtable source. Lorem Ipsum comes from sections 1.10.32 and 1.10.33 of "de Finibus Bonorum et Malorum" (The Extremes of Good and Evil) by Varrus, written in 45 BC. This book is a treatise on the theory of ethics, very popular during the Renaissance. The first line of Lorem Ipsum, "Lorem ipsum dolor sit amet..", comes from a line in section 1.10.32.</p>
  </div>
  <div class="footer"><span class="dot"></span>Legislative Council<span class="count">1/77</span></div>
</section>
</body>
</html>
```